If everything digital fails, here's what to do

Hi, I would like a poster / infographic of a list of practical actions people could take in case the internet stops working. I've put together a list of 8 areas, with the situation for each, and the mitigation actions folks can take - I need it presented in a clear and aesthetically pleasing way. I will send you the file with the full text so you can include it all

Target Market(s)

General population, but likely people who are safety conscious and want to protect themselves and learn more about what to do to be tech literate and prepared

Industry/Entity Type

Tech / Cyber / Public safety / Civic tech

Font styles to use
Sans Serif

Requirements
Must have
• It's a lot of text, so I think the important thing is to have it all in one poster, or in a series of similar pages
Nice to have
• I would like it to be a bit brooding, but also elicit competence and that some experts have thought about this and it will all be okay
Should not have
• I don't want it to look cartoonish, or cheap - less is more is sort of what I'm looking for

```html
<!DOCTYPE html>
<html lang="en">
<head>
<meta charset="utf-8">
<title>Information Management</title>
<link rel="stylesheet" href="https://fonts.googleapis.com/css2?family=Barlow+Semi+Condensed:wght@400;500;600;700&family=Barlow+Condensed:wght@600;700&display=swap">
<style>
:root{
  --ink-teal:#215563;
  --ribbon-teal:#45b0b9;
  --tab-teal:#1e7b7b;
  --refresh-blue:#4a78be;
  --note-bg:#e2ebf6;
  --note-ink:#2a5a68;
  --paper:#ffffff;
}
*{margin:0;padding:0;box-sizing:border-box}
html,body{width:848px;height:1200px;overflow:hidden;background:var(--paper)}
body{position:relative;font-family:"Barlow Semi Condensed",sans-serif}
.abs{position:absolute}

.title-band{left:105px;top:43px;width:743px;height:71px;background:var(--ink-teal)}
.title-text{left:137px;top:43px;height:71px;line-height:71px;color:#fff;font-family:"Barlow Semi Condensed",sans-serif;font-weight:700;font-size:55px;letter-spacing:1px;white-space:nowrap}
.title-badge{left:17px;top:24px;width:110px;height:110px}

.ribbon{width:621px;height:44px}
.ribbon-label{width:621px;text-align:center;color:#fff;font-family:"Barlow Condensed",sans-serif;font-weight:600;font-size:18px;line-height:40px;letter-spacing:.2px;text-shadow:1px 1px 1px rgba(0,0,0,.55)}
.tab-tail{left:117px;width:30px;height:17px;background:var(--tab-teal);border-radius:8px 0 0 8px}
.head-what{left:144px;width:194px;height:35px;background:var(--ink-teal);color:#fff;font-family:"Barlow Condensed",sans-serif;font-weight:600;font-size:26px;text-align:center;line-height:36px}
.head-refresh{left:510px;width:194px;height:38px;background:var(--refresh-blue);color:#fff;font-family:"Barlow Condensed",sans-serif;font-weight:600;font-size:26px;text-align:center;line-height:38px;text-shadow:1px 1px 1px rgba(0,0,0,.45)}

.action-panel{left:54px;width:389px;background:var(--ink-teal);border-radius:11px}
.action-body{left:64px;width:368px;border-radius:7px;background:linear-gradient(#2f5d6a,#8f9ea8);color:#fff;font-size:18px;line-height:23.4px;padding:6px 8px}
.refresh-panel{left:452px;width:346px;background:var(--refresh-blue);border-radius:12px}
.refresh-body{left:462px;width:327px;border-radius:7px;background:linear-gradient(#ffffff 5%,#7db5cf);color:var(--ink-teal);font-size:18px;line-height:23.4px;padding:6px 13px}

.safety-label{left:53px;top:375px;width:142px;height:31px;background:var(--ink-teal);border-radius:3px;color:#fff;font-family:"Barlow Condensed",sans-serif;font-weight:600;font-size:21px;line-height:31px;padding-left:12px}
.safety-note{left:92px;top:388px;width:720px;height:132px;background:var(--note-bg);border-radius:4px;color:var(--note-ink);font-size:15.5px;line-height:20.3px;padding:22px 10px 0 13px}
</style>
</head>
<body>

<div class="abs title-band"></div>
<svg class="abs title-badge" viewBox="0 0 110 110" aria-hidden="true">
  <circle cx="55" cy="54" r="50" fill="#fff" stroke="var(--ink-teal)" stroke-width="8"/>
  <g fill="var(--ribbon-teal)">
    <ellipse cx="52" cy="31" rx="29" ry="5"/>
    <path d="M23 35 Q52 42 81 35 V49 Q52 56 23 49Z"/>
    <path d="M23 54 Q52 61 81 54 V68 Q52 75 23 68Z"/>
    <path d="M23 73 Q52 80 81 73 V84 Q52 91 23 84Z"/>
  </g>
</svg>
<div class="abs title-text">INFORMATION MANAGEMENT</div>

<!-- Section: cloud storage -->
<svg class="abs ribbon" style="left:117px;top:152px" viewBox="0 0 621 44" aria-hidden="true">
  <path d="M0 4 Q0 0 4 0 H606 L620 21 L606 42 H0Z" fill="var(--ribbon-teal)"/>
</svg>
<div class="abs ribbon-label" style="left:117px;top:152px">CLOUDSTORAGE SERVICES HAVE STOPPED WORKING</div>
<div class="abs tab-tail" style="top:187px"></div>
<div class="abs head-what" style="top:187px">What to do?</div>
<div class="abs head-refresh" style="top:187px">Refresh when?</div>

<div class="abs action-panel" style="top:230px;height:131px"></div>
<div class="abs action-body" style="top:238px;height:106px">Do a backup of the important documents that are stored only in your cloud storage (e.g. that important email in your Postly; that tax docu­ment only issued digitally, etc.)</div>
<div class="abs refresh-panel" style="top:230px;height:79px"></div>
<div class="abs refresh-body" style="top:238px;height:61px">N/A once done</div>

<div class="abs safety-note">Note: Since this is a time-consuming exercise but not necessarily the same exercise as #7 below, you could alternate the months when you do one versus the other. For example, you could do this with annual equinoxes: March 21 and Sept 21 (pro tip: star email messages that are important as they arrive, so that you know what needs to be backed up every six months; that way, you don’t have to go searching through your whole inbox)</div>
<div class="abs safety-label">SAFETY NOTE:</div>

<!-- Section: password managers -->
<svg class="abs ribbon" style="left:117px;top:621px" viewBox="0 0 621 44" aria-hidden="true">
  <path d="M0 4 Q0 0 4 0 H606 L620 21 L606 42 H0Z" fill="var(--ribbon-teal)"/>
</svg>
<div class="abs ribbon-label" style="left:117px;top:621px">PASSWORD MANAGER SERVICES (CLOUD) HAVE STOPPED WORKING</div>
<div class="abs tab-tail" style="top:657px"></div>
<div class="abs head-what" style="top:657px;height:34px">What to do?</div>
<div class="abs head-refresh" style="top:657px;height:41px">Refresh when?</div>

<div class="abs action-panel" style="top:701px;height:242px"></div>
<div class="abs action-body" style="top:712px;height:196px">Preamble: Many individuals don’t remember their passwords anymore, having password managers generate complicated strings of characters as their passwords for their many digital accounts in their lives.<br>Print a full list of your accounts and their passwords and keep that document safely in your living space</div>
<div class="abs refresh-panel" style="top:704px;height:116px"></div>
<div class="abs refresh-body" style="top:712px;height:98px">Print a new such document every 6 months to ensure the list remains up to date</div>

</body>
</html>
```